Construction Company Facebook Banner

We are a small residential building company, building mostly new homes, renovations, extensions. our social media needs an uplift to look more professional.
I have no photos I wish to use in the banner as of yet however I have included the company logo, and the business card design which has some details.
I would like something simple but professional.
The banner does not need to have email, phone number, services provided etc. all of this is available on the facebook page itself. Something simple and clean please.
Industry/Entity Type
Construction
Requirements
Should not have
- Images of people, QR Code

```html
<!DOCTYPE html>
<html lang="en">
<head>
<meta charset="UTF-8">
<title>Creating Spaces For Life – Cover Banner</title>
<link href="https://fonts.googleapis.com/css2?family=Archivo:wght@400;700;800&display=swap" rel="stylesheet">
<style>
  :root {
    --page-bg: #a9bfae;
    --panel-light: #eeeff1;
    --panel-mid: #dcdee2;
    --ink: #222326;
    --ink-soft: #3a3b3f;
    --brand-green: #21a847;
    --brand-green-deep: #0f8a33;
    --slate: #5c5d60;
    --icon-grey: #6b6c6f;
  }
  * { box-sizing: border-box; margin: 0; padding: 0; }
  html, body {
    width: 1200px; height: 1000px; overflow: hidden;
    background: var(--page-bg);
    font-family: "Archivo", Arial, sans-serif;
  }
  .cover-banner {
    position: absolute;
    left: 50px; top: 291px;
    width: 1100px; height: 418px;
    background: linear-gradient(90deg, var(--panel-light) 0%, var(--panel-mid) 60%);
    overflow: hidden;
  }
  .cover-art { position: absolute; inset: 0; width: 100%; height: 100%; }
  .headline {
    position: absolute; left: 62px; top: 78px;
    color: var(--ink); line-height: 0.95;
  }
  .headline-line { display: block; text-transform: uppercase; }
  .headline-creating { font-weight: 700; font-size: 64px; letter-spacing: 0.5px; }
  .headline-spaces { font-weight: 800; font-size: 84px; color: var(--brand-green); letter-spacing: 0.5px; }
  .headline-forlife { font-size: 66px; display: flex; align-items: center; gap: 14px; }
  .headline-for { font-weight: 400; }
  .headline-life { font-weight: 800; margin-left: -6px; }
  .window-icon {
    display: grid; grid-template-columns: 1fr 1fr; gap: 4px;
    width: 48px; height: 48px;
  }
  .window-icon span { background: var(--icon-grey); }
  .services {
    position: absolute; left: 62px; top: 318px;
    font-size: 19px; color: var(--ink-soft);
    display: flex; align-items: center; gap: 10px;
  }
  .services .dot {
    width: 8px; height: 8px; border-radius: 50%;
    background: var(--brand-green);
  }
</style>
</head>
<body>
  <section class="cover-banner">
    <svg class="cover-art" viewBox="0 0 1100 418" preserveAspectRatio="none">
      <defs>
        <linearGradient id="sketchTone" x1="0" y1="0" x2="1" y2="1">
          <stop offset="0" stop-color="#e4e5e7"/>
          <stop offset="1" stop-color="#c9cacd"/>
        </linearGradient>
        <linearGradient id="photoTone" x1="0" y1="0" x2="0" y2="1">
          <stop offset="0" stop-color="#c9a08f"/>
          <stop offset="0.3" stop-color="#9aa3ad"/>
          <stop offset="0.6" stop-color="#6e7580"/>
          <stop offset="0.82" stop-color="#8a6a45"/>
          <stop offset="1" stop-color="#2f5a2a"/>
        </linearGradient>
      </defs>
      <polygon points="560,0 800,0 720,418 430,418" fill="url(#sketchTone)"
               role="img" aria-label="Architectural line sketch of a two-storey house"/>
      <polygon points="790,0 1100,0 1100,418 700,418" fill="url(#photoTone)"
               role="img" aria-label="Photo of a modern two-storey weatherboard home at dusk with lit windows and garden"/>
      <polygon points="590,70 410,418 600,418" fill="var(--slate)" opacity="0.7"/>
      <polygon points="640,0 880,0 770,150 560,150" fill="var(--brand-green)" opacity="0.95"/>
      <polygon points="520,250 700,250 810,418 610,418" fill="var(--brand-green-deep)" opacity="0.85"/>
    </svg>

    <h1 class="headline">
      <span class="headline-line headline-creating">Creating</span>
      <span class="headline-line headline-spaces">Spaces</span>
      <span class="headline-line headline-forlife">
        <span class="headline-for">For</span>
        <span class="headline-life">Life</span>
        <span class="window-icon" aria-hidden="true"><span></span><span></span><span></span><span></span></span>
      </span>
    </h1>

    <p class="services">
      <span>New Homes</span><span class="dot"></span>
      <span>Renovations</span><span class="dot"></span>
      <span>Extensions</span>
    </p>
  </section>
</body>
</html>
```